Corvane Networks web design

Corvane is an Internet Service Provider bringing high-speed service to homes and businesses. Our principal market target is rural areas of West Michigan, but we intend to expand rapidly. We need a website to market our services, facilitate online ordering, customer support and communicate with our customers.

I will upload a draft outline of the content we hope to include in the website.

We compete directly with Halberd Communications, Lumetra, Dravix and Kelwick communications to bring Internet service to homes and businesses in our coverage area.

Our primary values include:

1. Unlike our competitors, we do not require long term contractors or service bundles; There are no termination fees, for example. All services are sold on a recurring 1-month agreement term.
2. Unlike other wireless (mobile) providers, we do not limit downloads or uploads with bit/byte buckets
3. We provide service to areas ignored by the larger carriers - Rural areas in Michigan that lack options for broadband are prime targets for Corvane to cover.
4. Unlike other wireless ISP's, we utilize licensed FCC spectrum. We do not use unlicensed/free frequencies, providing us an advantage for reliability and stability.
Updates

So many wonderful designs, thank you very much for all your hard work. We are evaluating all our favorite designs and plan to make a selection in the next 2 days. I will be in touch with you to request revisions if necessary or further refinements.  Thank you again for your efforts on this project.

Target Market(s)

Our target market is home Internet users. however, that does not mean that our users are "high tech" oriented - they are just normal mom's and pop's who buy Internet for home use. The site should be easy to navigate and communicate our message of speed, value, reliability and facilitate simple product ordering.

Industry/Entity Type

Internet

Requirements
Must have
• Our phone number should be prominently displayed 1-844-7NU-LINK
• Our logo is uploaded in the attachments.
• Design for desktop and mobile devices.
Nice to have
• The most modern of web design trends. Such as a design that facilitates parallax scrolling effects rather than lots of individual pages.
• Stock artwork communicating our values of speed and reliability.

```html
<!DOCTYPE html>
<html lang="en">
<head>
<meta charset="utf-8">
<title>Corvane Networks — West Michigan's Best Internet Service</title>
<link href="https://fonts.googleapis.com/css2?family=Open+Sans:wght@400;600;700&display=swap" rel="stylesheet">
<style>
:root{
  --orange:#f7941d;
  --orange-deep:#ef7f0a;
  --orange-soft:#fde3c4;
  --charcoal:#3a3a3a;
  --charcoal-dark:#2b2b2b;
  --panel:#f3f3f3;
  --line:#e2e2e2;
  --text:#555;
  --muted:#888;
  --white:#fff;
}
*{box-sizing:border-box;margin:0;padding:0}
html,body{width:1200px;height:2280px;overflow:hidden}
body{font-family:"Open Sans",Arial,sans-serif;color:var(--text);background:var(--white);font-size:13px;line-height:1.5;position:relative}
.wrap{width:920px;margin:0 auto;position:relative}

/* header */
.site-header{background:var(--orange);height:170px}
.brand{position:absolute;left:0;top:28px;color:var(--white);font-weight:700;font-size:30px;letter-spacing:3px;line-height:1}
.brand small{display:block;font-size:30px}
.top-right{position:absolute;right:0;top:18px;text-align:right}
.social{display:flex;gap:8px;justify-content:flex-end}
.social span{width:22px;height:22px;border-radius:50%;background:var(--white);opacity:.9}
.call{margin-top:14px;color:var(--white);font-size:22px;font-weight:600;display:flex;align-items:center;gap:8px;justify-content:flex-end}
.main-nav{position:absolute;left:0;top:120px;width:920px;height:44px;background:var(--charcoal);display:flex;align-items:center}
.main-nav a{color:var(--white);text-decoration:none;font-size:14px;padding:0 26px;height:44px;line-height:44px;border-right:1px solid #555}
.main-nav a.active{background:var(--charcoal-dark)}
.search{margin-left:auto;margin-right:10px;width:170px;height:26px;background:var(--white);border-radius:2px;position:relative}
.search::after{content:"";position:absolute;right:0;top:0;width:26px;height:26px;background:var(--orange)}

/* hero */
.hero{height:310px;display:flex;border:1px solid var(--line);border-top:0}
.hero-art{width:720px;height:100%;position:relative;background:linear-gradient(120deg,#ffffff 0%,#eef0f2 45%,#d9dde1 100%)}
.hero-copy{position:absolute;right:40px;top:60px;width:250px;text-align:center}
.hero-copy h1{font-size:28px;line-height:1.2;color:#333;font-weight:600}
.hero-copy h1 .accent{background:var(--orange);color:var(--white);padding:0 6px}
.hero-copy p{margin-top:14px;font-size:11px;color:#444}
.hero-values{width:200px;background:var(--panel);display:flex;flex-direction:column;align-items:center;justify-content:space-around;padding:10px 0}
.value{text-align:center;font-size:13px;color:#444}
.value .dot{width:64px;height:64px;border-radius:50%;background:var(--orange);margin:0 auto 6px;display:flex;align-items:center;justify-content:center}

/* welcome */
.welcome{padding:40px 0 20px;text-align:center}
.welcome h2,.section-title{color:var(--orange);font-size:20px;font-weight:600}
.welcome p{margin-top:14px;font-size:12px;text-align:left;color:var(--muted)}

/* feature columns */
.features{display:flex;gap:20px;margin-top:20px}
.feature{flex:1;border:1px solid var(--line);height:300px}
.feature h3{font-size:14px;color:var(--orange);font-weight:600;padding:12px 14px;border-bottom:1px solid var(--line)}
.feature ul{list-style:none;padding:12px 14px}
.feature li{font-size:12px;color:var(--muted);padding:5px 0 5px 18px;position:relative}
.feature li::before{content:"";position:absolute;left:0;top:11px;width:8px;height:8px;background:var(--orange);border-radius:50%}

/* plans */
.plans-block{margin-top:90px;text-align:center}
.plans{display:flex;gap:40px;margin-top:24px}
.plan{flex:1;background:var(--orange);color:var(--white);height:230px;padding:20px 30px;text-align:center}
.plan h3{font-size:26px;font-weight:600}
.plan .lead{font-size:11px;margin-top:8px}
.plan ul{list-style:none;margin-top:12px}
.plan li{font-size:12px;padding:5px 0;border-bottom:1px solid rgba(255,255,255,.35)}
.btn{display:inline-block;margin-top:14px;background:var(--white);color:var(--orange);font-weight:600;font-size:12px;padding:4px 22px;border-radius:3px}

/* latest */
.latest{display:flex;gap:20px;margin-top:40px}
.latest-col{flex:1;border:1px solid var(--line);height:310px}
.latest-col h3{background:var(--orange);color:var(--white);font-size:14px;font-weight:600;padding:8px 14px}
.entry{display:flex;gap:10px;padding:12px 14px 6px;font-size:11px;color:var(--muted)}
.entry .ic{width:14px;height:14px;flex:none;margin-top:2px}
.entry .thumb{width:60px;height:52px;flex:none;background:linear-gradient(135deg,#2c3e5a,#6f8fb8)}
.entry a{color:var(--orange)}

/* footer */
.footer-bar{position:absolute;left:0;top:1800px;width:1200px;height:40px;background:var(--orange)}
.footer-bar nav{display:flex;justify-content:space-between;width:620px;margin:0 auto;line-height:40px}
.footer-bar a{color:var(--white);text-decoration:none;font-size:12px}
.footer-main{position:absolute;left:0;top:1840px;width:1200px;height:390px;background:var(--charcoal)}
.footer-cols{display:flex;gap:30px;padding-top:40px}
.footer-col{flex:1;color:#ccc;font-size:11px}
.footer-col h4{color:var(--white);font-size:12px;font-weight:600;margin-bottom:12px}
.footer-col li{list-style:none;padding:3px 0}
.footer-col li::before{content:"› ";color:var(--orange)}
.footer-brand{color:var(--white);font-weight:700;font-size:22px;letter-spacing:3px;text-align:right}
.copyright{position:absolute;left:0;top:2230px;width:1200px;height:50px;background:var(--charcoal-dark);color:#aaa;font-size:10px;text-align:center;line-height:50px}
</style>
</head>
<body>
<header class="site-header">
  <div class="wrap">
    <div class="brand">CORVANE<small>NETWORKS</small></div>
    <div class="top-right">
      <div class="social"><span></span><span></span><span></span><span></span><span></span></div>
      <div class="call">
        <svg width="20" height="20" viewBox="0 0 24 24" fill="#fff"><path d="M6.6 10.8a15 15 0 0 0 6.6 6.6l2.2-2.2c.3-.3.7-.4 1-.2 1.1.4 2.3.6 3.6.6.6 0 1 .4 1 1V20c0 .6-.4 1-1 1A17 17 0 0 1 3 4c0-.6.4-1 1-1h3.5c.6 0 1 .4 1 1 0 1.3.2 2.5.6 3.6.1.3 0 .7-.2 1z"/></svg>
        Call - 1-844-7NU-LINK
      </div>
    </div>
    <nav class="main-nav">
      <a class="active" href="#">Home</a><a href="#">Service Plans</a><a href="#">Coverage Map</a><a href="#">About Us</a>
      <div class="search"></div>
    </nav>
  </div>
</header>

<main class="wrap">
  <section class="hero">
    <div class="hero-art" role="img" aria-label="Illustration of a connected network of homes and towers">
      <div class="hero-copy">
        <h1>West Michigan's<br><span class="accent">Best Internet Service</span></h1>
        <p>FCC Licensed reliability. Corvane 4G utilizes the latest wireless technologies using FCC licensed frequencies, signals move faster.</p>
      </div>
    </div>
    <aside class="hero-values">
      <div class="value"><div class="dot"><svg width="30" height="30" viewBox="0 0 24 24" fill="#fff"><path d="M13 2 4 14h7l-1 8 9-12h-7z"/></svg></div>Faster Speed</div>
      <div class="value"><div class="dot"><svg width="34" height="20" viewBox="0 0 34 20" fill="none" stroke="#fff" stroke-width="3"><path d="M9 10c0-4 6-4 8 0s8 4 8 0-6-4-8 0-8 4-8 0z"/></svg></div>No Limits</div>
      <div class="value"><div class="dot"><svg width="30" height="30" viewBox="0 0 24 24" fill="none" stroke="#fff" stroke-width="2.4"><path d="M12 3v18M16 7c-1-1.5-7-2-7 1.5S16 11 16 15s-6 3-7 1"/></svg></div>More Value</div>
    </aside>
  </section>

  <section class="welcome">
    <h2>Welcome To Michigan's Best Internet Service</h2>
    <p>Corvane brings fast, dependable internet to homes and businesses across rural West Michigan, where larger carriers have left families without real options. We run on licensed FCC spectrum for a steady signal, never cap your downloads or uploads, and sell every plan on a simple month to month term with no contracts, no bundles and no termination fees. Our local team installs, supports and stands behind every connection we build.</p>
  </section>

  <section class="features">
    <div class="feature">
      <h3>West Michigan's Best Internet Service</h3>
      <ul>
        <li>100% Satisfaction Guaranteed</li>
        <li>Easiest Pricing, No Hidden Fees</li>
        <li>No Long Term Contracts</li>
        <li>No Phone Line or Cable TV required</li>
        <li>Fast Speeds, Residential and Business</li>
        <li>Interference Free FCC Licensed 4G Coverage</li>
      </ul>
    </div>
    <div class="feature">
      <h3>Why Corvane?</h3>
      <ul>
        <li>No Download Limits: Stream and browse all you want with no data buckets.</li>
        <li>FCC licensed reliability: Corvane 4G utilizes the latest wireless technologies using FCC licensed frequencies.</li>
      </ul>
    </div>
    <div class="feature">
      <h3>Buy Local</h3>
      <ul>
        <li>Corvane is Local: We're a locally owned and operated business. We're here for our neighbors in West Michigan.</li>
        <li>Best Value, Best For You: Better value and faster speeds than the big carriers, plus support you can actually reach.</li>
      </ul>
    </div>
  </section>

  <section class="plans-block">
    <h2 class="section-title">Service Plans</h2>
    <div class="plans">
      <div class="plan">
        <h3>Residential Plans</h3>
        <p class="lead">Unlimited download and upload - no contract, no 2 year term.<br>Simple Apps enabled email accounts</p>
        <ul>
          <li>1.5/0.5 Mb / month $49.99 install</li>
          <li>3/1 Mb / month $59.99 install</li>
          <li>5/1.5 Mb / month $69.99 install</li>
        </ul>
        <span class="btn">Sign up</span>
      </div>
      <div class="plan">
        <h3>Business Plans</h3>
        <p class="lead">Unlimited download and upload - no contract, no 2 year term.<br>Simple Apps enabled email accounts</p>
        <ul>
          <li>1.5/0.5 Mb / month $99.99 install</li>
          <li>3/1 Mb / month $129.99 install</li>
          <li>5/1.5 Mb / month $159.99 install</li>
        </ul>
        <span class="btn">Sign up</span>
      </div>
    </div>
  </section>

  <section class="latest">
    <div class="latest-col">
      <h3>Latest News</h3>
      <div class="entry"><svg class="ic" viewBox="0 0 14 14"><rect width="14" height="14" fill="#f7941d"/></svg><div>New towers bring coverage to more rural homes this spring.<br><a href="#">Read more</a></div></div>
      <div class="entry"><svg class="ic" viewBox="0 0 14 14"><rect width="14" height="14" fill="#f7941d"/></svg><div>Corvane adds faster plans with no change to monthly terms.<br><a href="#">Read more</a></div></div>
      <div class="entry"><svg class="ic" viewBox="0 0 14 14"><rect width="14" height="14" fill="#f7941d"/></svg><div>Local support hours extended for evening callers.<br><a href="#">Read more</a></div></div>
    </div>
    <div class="latest-col">
      <h3>Latest Tweets</h3>
      <div class="entry"><svg class="ic" viewBox="0 0 14 14"><circle cx="7" cy="7" r="7" fill="#f7941d"/></svg><div>Installs are booking fast in Allegan county, call today.<br><a href="#">2 hours ago</a></div></div>
      <div class="entry"><svg class="ic" viewBox="0 0 14 14"><circle cx="7" cy="7" r="7" fill="#f7941d"/></svg><div>No caps, no contracts, just steady internet at home.<br><a href="#">1 day ago</a></div></div>
      <div class="entry"><svg class="ic" viewBox="0 0 14 14"><circle cx="7" cy="7" r="7" fill="#f7941d"/></svg><div>Check the coverage map to see if your road is online.<br><a href="#">3 days ago</a></div></div>
    </div>
    <div class="latest-col">
      <h3>Latest Blog</h3>
      <div class="entry"><div class="thumb" role="img" aria-label="Blog photo of a wireless tower"></div><div>Why licensed spectrum keeps your signal steady.<br><a href="#">Read more</a></div></div>
      <div class="entry"><div class="thumb" role="img" aria-label="Blog photo of a family online at home"></div><div>Streaming at home without data buckets.<br><a href="#">Read more</a></div></div>
      <div class="entry"><div class="thumb" role="img" aria-label="Blog photo of rural farmland"></div><div>Bringing broadband to the back roads.<br><a href="#">Read more</a></div></div>
    </div>
  </section>
</main>

<div class="footer-bar">
  <nav><a href="#">Home</a><a href="#">About us</a><a href="#">Services</a><a href="#">Coverage</a><a href="#">Blog</a></nav>
</div>
<footer class="footer-main">
  <div class="wrap footer-cols">
    <div class="footer-col"><h4>MENU</h4><ul><li>Service Plans</li><li>Coverage Map</li><li>Company Blog</li><li>Customer Support</li><li>Account Management</li></ul></div>
    <div class="footer-col"><h4>CONTACTS</h4><p>Call today to place an order<br>Customer support:<br>1-844-7NU-LINK<br>Local number:<br>616-555-0142<br>Email support:<br>help@corvanenet.com</p></div>
    <div class="footer-col"><h4>ADDRESS</h4><p>Corvane Networks, LLC<br>4582 Orchard Avenue<br>Grand Landing, MI 49507</p></div>
    <div class="footer-col"><h4>SUPPORT STAFF HOURS</h4><p>Weekdays: 8am to 10pm<br>Weekends: 9am to 6pm<br>Holiday schedule varies</p></div>
    <div class="footer-col"><div class="footer-brand">CORVANE</div></div>
  </div>
</footer>
<div class="copyright">Copyright 2014 Corvane Networks. All Rights Reserved.</div>
</body>
</html>
```